Brochure design for International Beauty Trade Show

I neee a tri-fold company products' brochure to distribute to customers at an international trade show coming soon. We have 4 main product categories- hair and skincare, facial care, Body and bath and massage oil.
The brochure needs to include at least 2 photos of the main products of each category, benefits, call to action and our company contact info ( website and phone number).

Target Market(s)

Educated and high income earners looking for all-natural,pure, 100 organic products for their beauty and personal care needs. Our products cross all racial groups/demographics and suitable for all skin types

Industry/Entity Type

Hair And Beauty

Font styles to use
Serif

Colors

Designer to choose colors to be used in the design.

Requirements
Must have
• The design must stand out as pure and luxury and at the same time be inclusive using our logo design colors- orange and blue. Also, the content must be easy to read and captivating.
• Finally if using women pictures, please include Black, white, Asian and Latina to reflect the fact that our products are suitable for all skin types.
Nice to have
• Design the brochure such that it could be printed as a poster-banner ad.
Should not have
• Cookie cutter designs are not welcome

```html
<!DOCTYPE html>
<html lang="en">
<head>
<meta charset="utf-8">
<title>Navara Soins – Product Brochure</title>
<link rel="stylesheet" href="https://fonts.googleapis.com/css2?family=Lato:wght@300;400;700&family=Tinos&display=swap">
<style>
  :root{
    --page-bg:#e9e9e9;
    --sheet:#fbfcfc;
    --ink:#333;
    --ink-soft:#4a4a4a;
    --orange:#ee7428;
    --blue:#1e8bcb;
    --rule:#555;
  }
  *{box-sizing:border-box;margin:0;padding:0}
  html,body{width:1200px;height:1000px;overflow:hidden;background:var(--page-bg)}
  .sheet{position:absolute;left:101px;top:119px;width:996px;height:770px;background:var(--sheet);font-family:"Lato",sans-serif;color:var(--ink-soft);box-shadow:0 6px 24px rgba(0,0,0,.25)}
  .photo{position:absolute}
  .photo-carrot{left:0;top:0;width:337px;height:201px;background:linear-gradient(180deg,#eef0ec 0%,#cfd2cb 50%,#6a6a62 80%,#3a3a34 100%)}
  .photo-soap{left:666px;top:0;width:330px;height:204px;background:linear-gradient(160deg,#f6f6f4 0%,#e2e4e0 55%,#ecd2ac 100%)}
  .photo-portrait{left:666px;top:569px;width:330px;height:201px;background:linear-gradient(90deg,#2a2826 0%,#1e1c1b 55%,#6a4a3a 100%)}
  .brand{position:absolute;font-family:"Tinos",serif;font-size:11px;color:#fff;letter-spacing:.5px}
  .brand-dark{color:#555}
  .caption{position:absolute;font-family:"Tinos",serif;color:#222;line-height:1}
  .caption small{display:block;line-height:.8}
  .section{position:absolute}
  .section h2{position:relative;font-weight:700;font-size:22px;color:var(--ink);padding-left:var(--pad,17px);line-height:1;white-space:nowrap}
  .section h2::before{content:"";position:absolute;left:0;top:-10px;width:var(--bar,11px);height:42px;background:var(--accent)}
  .section ul{list-style:none;margin-top:26px}
  .section li{position:relative;font-weight:300;font-size:16.5px;padding-left:15px;line-height:29.8px;color:var(--ink-soft);white-space:nowrap}
  .section li::before{content:"";position:absolute;left:-1px;top:13px;width:5px;height:5px;border-radius:50%;background:#555}
  .orange{--accent:var(--orange)}
  .blue{--accent:var(--blue)}
  .product{position:absolute;border-radius:10px}
  .rule{position:absolute;left:364px;top:391px;width:266px;height:1px;background:var(--rule)}
</style>
</head>
<body>
<main class="sheet">
  <div class="photo photo-carrot" role="img" aria-label="Carrot oil bottle with candles, spa stones and fresh carrots"></div>
  <span class="brand brand-dark" style="left:12px;top:18px">Navara Soins</span>
  <div class="caption" style="left:122px;top:17px;font-size:14px">Huile de Carotte<small style="font-size:8px;letter-spacing:2px;margin-top:4px">Visage &amp; Corps</small></div>

  <section class="section orange" style="left:336px;top:36px">
    <h2>Facial Care</h2>
    <ul style="margin-left:34px">
      <li>Reduce sebum secretion</li>
      <li>Eliminate toxins &amp; blemishes</li>
      <li>Tighten pores</li>
      <li>Dry pimples</li>
      <li>Remove blackheads</li>
    </ul>
  </section>
  <div class="product" role="img" aria-label="Facial clay mask jar" style="left:381px;top:264px;width:93px;height:92px;border-radius:14px;background:linear-gradient(#f4f4f2,#dcdad3)"></div>
  <div class="product" role="img" aria-label="Facial clay box with green powder" style="left:504px;top:279px;width:115px;height:74px;background:linear-gradient(#d3e6d3,#a8c6ab)"></div>
  <div class="rule"></div>

  <section class="section blue" style="left:0;top:268px;--bar:21px;--pad:27px">
    <h2>Hair &amp; Skincare</h2>
    <ul style="margin-left:37px">
      <li>Anti-Aging, remove wrinkles</li>
      <li>Natural moisturizer</li>
      <li>Heal damaged hair or sensitive scalp</li>
      <li>Soften curly and frizzy hair</li>
      <li>Reduce sebum secretion</li>
      <li>Tone, soothe and restore luster</li>
      <li>Restore fair complexion</li>
    </ul>
  </section>
  <div class="product" role="img" aria-label="Four argan oil pump bottles" style="left:74px;top:541px;width:195px;height:166px;background:linear-gradient(90deg,#d6a06a,#b06a34 30%,#c98a4f 55%,#a8652f 80%,#d6a06a)"></div>

  <section class="section blue" style="left:336px;top:434px;--pad:19px">
    <h2>Massage Care</h2>
    <ul style="margin-left:28px;margin-top:8px">
      <li>Relief stress and pain</li>
      <li>Fight muscle contraction/tenderness</li>
      <li>Eliminate stretch marks</li>
      <li>Pure, natural undiluted</li>
    </ul>
  </section>
  <div class="product" role="img" aria-label="Black soap jar" style="left:398px;top:636px;width:76px;height:78px;border-radius:12px;background:linear-gradient(#3a3f4c,#151820)"></div>
  <div class="product" role="img" aria-label="Massage oil spray bottle with red berries" style="left:516px;top:599px;width:118px;height:122px;background:linear-gradient(135deg,#5a3a30,#9a3030 70%,#e7e3e0)"></div>

  <div class="photo photo-soap" role="img" aria-label="Argan soap jar with candles, orange slice and blossom"></div>
  <span class="brand brand-dark" style="left:845px;top:92px">Navara Soins</span>
  <div class="caption" style="left:856px;top:154px;font-size:22px">Savon argan<small style="font-size:13px">flore d’oranger</small></div>

  <section class="section orange" style="left:666px;top:242px">
    <h2>Body&nbsp; &amp; Bath Care</h2>
    <ul style="margin-left:35px">
      <li>Purify and disinfect</li>
      <li>Fight&nbsp; acne</li>
      <li>Rejuvenate &amp; hydrate</li>
      <li>Promote healthy looking skin</li>
      <li>Remove dead cells</li>
    </ul>
  </section>
  <div class="product" role="img" aria-label="Body scrub jar with red clay" style="left:731px;top:459px;width:75px;height:70px;background:linear-gradient(#8a8a8a,#b5553a)"></div>
  <div class="product" role="img" aria-label="Lemon soap box with lemons" style="left:847px;top:461px;width:102px;height:68px;background:linear-gradient(#b9d4a0,#e6d85a)"></div>

  <div class="photo photo-portrait" role="img" aria-label="Model portrait with facial oil bottle and prickly pear fruit"></div>
  <span class="brand" style="left:686px;top:597px;font-size:12px">Navara Soins</span>
</main>
</body>
</html>
```